Coaching Workbook (for life & health coaching industry)

I created a coaching workbook using Canva. I would like it recreated more professionally in PowerPoint with better images and creative design using my 3 branding colors (teal primary, salmon secondary, and turquoise splash here and there).

Please use the attached image of lady sitting on dock at the lake on the first slide for the cover along with my logo and my titles (similar to my Canva version on my website).

My version of the workbook is attached. Thank you for turning my drab into fab:-) Mavis Ketterwell, Life & Health Coach, Grief Recovery Specialist
Updates

To ensure clarity, I am looking for a PowerPoint (prefer vertical format) for a coaching manual FROM the material in the version that I created in Canva, which is currently on my website as a download at the bottom of my coaching page: https://brightpathwayguide.example/coaching-2 I will upload the pdf file as well as the example that I'm trying to recreate in PowerPoint, but more professionally and creatively. Thank You! Mavis Ketterwell

Target Market(s)

My target audience is primarily female, with a few males each year, ages range from mid-twenties to sixties. Everyone will experience the pain of loss and grief. Women are more prone to reach out for help sooner.

Industry/Entity Type

Life Coaching

Font styles to use
Serif

Requirements
Must have
• Want it to feel personal, not corporate if that makes sense.
• Must use my 3 branding colors: HEX # 2994ae, 10dfd3, fa8070.
• Please use Playfair Display font for consistency with my website.
• The text for the workbook is included in the Word document attached below.
Should not have
• I'm not looking for the material on my website to be the focus of this workbook. I want the Canva version that I created to be converted more professionally and creatively in PowerPoint, so I can manage moving forward.

```html
<!DOCTYPE html>
<html lang="en">
<head>
<meta charset="utf-8">
<title>Coaching Workbook – Slides 5 to 8</title>
<link href="https://fonts.googleapis.com/css2?family=Playfair+Display:wght@900&family=Poppins:wght@300;400;500&display=swap" rel="stylesheet">
<style>
  :root {
    --stage: #3a3b3d;
    --salmon: #fa8070;
    --teal: #2994ae;
    --turquoise: #10dfd3;
    --wheel-blue: #3aa9e0;
    --ink: #3c3c3c;
    --paper: #ffffff;
    --rule: #bdbdbd;
  }
  * { margin: 0; padding: 0; box-sizing: border-box; }
  html, body { width: 1200px; height: 1200px; overflow: hidden; background: var(--stage); }
  .canvas { position: relative; width: 1200px; height: 1200px; background: var(--stage); font-family: "Poppins", sans-serif; color: var(--ink); }

  .slide { position: absolute; width: 432px; height: 568px; background: var(--paper); overflow: hidden; }
  .slide--journaling { left: 34px; top: 32px; }
  .slide--wheel { left: 491px; top: 32px; }
  .slide--why { left: 34px; top: 610px; }
  .slide--values { left: 491px; top: 610px; }

  .slide__header { background: var(--salmon); color: var(--paper); font-family: "Playfair Display", serif; font-weight: 900; text-align: center; display: flex; align-items: center; justify-content: center; font-size: 27px; letter-spacing: 0.2px; }
  .slide--journaling .slide__header { height: 62px; }
  .slide--wheel .slide__header { height: 51px; }
  .slide--why .slide__header, .slide--values .slide__header { height: 40px; }

  .photo { position: absolute; left: 0; width: 100%; }
  .photo--writer { top: 62px; height: 286px; background: linear-gradient(180deg, #3f3f3f 0%, #5a6f8c 45%, #c9a23a 78%, #7a6a4a 100%); }
  .photo--group { top: 40px; height: 306px; background: linear-gradient(90deg, #4d5566 0%, #6b6f74 35%, #d8d1c6 60%, #4c5f7c 80%, #b9b24a 100%); }
  .photo--compass { top: 40px; height: 286px; background: radial-gradient(circle at 62% 70%, #8a6a45 0%, #5d4a3a 25%, #6f8a9c 60%, #3d5466 100%); }

  .card { position: absolute; background: var(--paper); box-shadow: 0 1px 4px rgba(0,0,0,0.25); padding: 16px 7px 10px; font-size: 7.3px; line-height: 1.45; }
  .card p { margin-bottom: 10px; }
  .card p:last-child { margin-bottom: 0; }
  .card--journaling { left: 16px; top: 267px; width: 400px; height: 287px; }
  .card--why { left: 30px; top: 332px; width: 373px; height: 178px; padding: 14px 6px; }
  .card--values { left: 18px; top: 286px; width: 397px; height: 264px; padding: 14px 6px; }
  .quote { color: var(--teal); }
  .link { color: var(--teal); text-decoration: underline; }
  .card__lead { color: var(--salmon); font-size: 9.5px; font-weight: 500; margin-bottom: 14px !important; }

  .wheel { position: absolute; left: 0; top: 51px; width: 432px; height: 330px; }
  .wheel text { font-family: "Poppins", sans-serif; font-size: 7.5px; fill: #333; text-anchor: middle; }
  .wheel-copy { position: absolute; left: 38px; top: 362px; width: 356px; text-align: center; font-size: 7.3px; line-height: 1.5; }
  .wheel-copy p { margin-bottom: 14px; }
  .wheel-copy .note { color: var(--salmon); font-weight: 500; text-transform: uppercase; letter-spacing: 0.4px; }
  .num { color: var(--salmon); }

  .slide-range { position: absolute; left: 1052px; top: 520px; transform: translate(-50%, -50%) rotate(-90deg); font-family: "Poppins", sans-serif; font-weight: 300; font-size: 150px; color: var(--salmon); white-space: nowrap; letter-spacing: 2px; line-height: 1; }
</style>
</head>
<body>
<div class="canvas">

  <section class="slide slide--journaling">
    <h2 class="slide__header">Benefits of Journaling</h2>
    <div class="photo photo--writer" role="img" aria-label="Photo of a young man in glasses writing in a journal on a yellow sofa"></div>
    <div class="card card--journaling">
      <p>Have you made journaling a part of your daily well-being routine yet? If not, you might be thinking, “No – I’m not a great writer.” <span class="quote">Or even, “I really don’t like writing. Why would I journal?”</span></p>
      <p>Journaling is not about writing. It’s about providing you with a deeper understanding of your life.</p>
      <p>Trust me, I’m not a gifted writer. English was my most difficult subject in school. It wasn’t until I was in my thirties that I discovered the benefits of journaling. In my journal, my writing didn’t have to be perfect. It wasn’t about receiving a passing grade. Journaling helped me sort out my past, let go of what was no longer serving me, and start living more in the present. It provided a great outlet for my monkey mind before bedtime, so that I could sleep more easily.</p>
      <p>Often, journaling was, for me, just a brain dump on paper. Yet, it has led to so many gifts. Most importantly, it gave me a profound insight into my mind and desires.</p>
      <p>Spending time in this quiet self-reflection helped me shed the blanket of shame I had been living under for so long. Replacing unhealthy and damaging thoughts became easier. And with a clearer mind, my creativity began to flow. I tapped into more courage. And a desire to connect with others on a similar path fueled my passion for coaching.</p>
      <p>Want to experience the <span class="link">benefits of journaling</span>? Check out a free, password protected online digital journal at <span class="link">Inkleaf.example</span></p>
    </div>
  </section>

  <section class="slide slide--wheel">
    <h2 class="slide__header">Life Satisfaction</h2>
    <svg class="wheel" viewBox="0 0 432 330" aria-label="Wheel of life rating chart from 0 to 10">
      <circle cx="215" cy="153" r="114" fill="var(--wheel-blue)"/>
      <circle cx="215" cy="153" r="58" fill="#fff"/>
      <g fill="none" stroke="#5cb8e6" stroke-width="0.6">
        <circle cx="215" cy="153" r="72"/><circle cx="215" cy="153" r="86"/><circle cx="215" cy="153" r="100"/>
      </g>
      <g fill="none" stroke="#cfcfcf" stroke-width="0.6">
        <circle cx="215" cy="153" r="14"/><circle cx="215" cy="153" r="29"/><circle cx="215" cy="153" r="43"/>
      </g>
      <g stroke="#cfcfcf" stroke-width="0.6">
        <line x1="215" y1="39" x2="215" y2="267"/><line x1="101" y1="153" x2="329" y2="153"/>
        <line x1="134" y1="72" x2="296" y2="234"/><line x1="296" y1="72" x2="134" y2="234"/>
      </g>
      <text x="215" y="9" fill="#333">........................</text>
      <text x="215" y="44">10</text><text x="215" y="272">10</text>
      <text x="111" y="156">10</text><text x="319" y="156">10</text>
      <text x="134" y="79">10</text><text x="296" y="79">10</text>
      <text x="134" y="238">10</text><text x="296" y="238">10</text>
      <text x="145" y="90">8</text><text x="286" y="90">8</text><text x="145" y="227">8</text><text x="286" y="227">8</text>
      <text x="159" y="103">6</text><text x="272" y="103">6</text><text x="157" y="215">6</text><text x="272" y="215">6</text>
      <text x="181" y="125">2</text><text x="249" y="125">2</text><text x="181" y="186">2</text><text x="249" y="186">2</text>
      <text x="215" y="156">0</text>
      <text x="83" y="55">.........................</text><text x="345" y="61">.........................</text>
      <text x="55" y="156">..............</text><text x="371" y="156">..............</text>
      <text x="84" y="279">.........................</text><text x="345" y="285">.........................</text>
      <text x="215" y="316">........................</text>
    </svg>
    <div class="wheel-copy">
      <p>A big part of transforming your life involves assessing where you are right now. It’s asking yourself, <span class="quote">“How satisfied am I with my life?”</span></p>
      <p>The wheel of life exercise is a great starting point for evaluating your life. It’s a self-reflection exercise that helps you build in more balance, happiness, and success to your daily life. It also brings your attention to all the different areas of your life and helps you prioritize your goals.</p>
      <p>Complete the wheel of life below, labeling the eight most important areas of your life in each blank around the circle. Then, rate your level of satisfaction from <span class="num">0</span> (the least satisfied) to <span class="num">10</span> (the most satisfied).</p>
      <p class="note">Create wheel of life image here similar to the one I copied off the internet.</p>
    </div>
  </section>

  <section class="slide slide--why">
    <h2 class="slide__header">Understand Your Why</h2>
    <div class="photo photo--group" role="img" aria-label="Photo of a group of people in casual clothes standing side by side, shown from the shoulders down"></div>
    <div class="card card--why">
      <p>Cognitive clarity is an integral component of getting the most out of life coaching!</p>
      <p>Cognitive clarity means understanding your why. Learning what motivates you and influences your decisions and actions is not only key to making successful life changes, it’s also what gives you an idea of what makes you tick and why.</p>
      <p>Our brains are gifted with the ability to make new and improved neural pathways throughout our life. My goal as your coach is to help you connect with your why on a deeper level and foster healthier connections as you continue working on your goals.</p>
      <p><span class="link">Read more about understanding your why.</span></p>
    </div>
  </section>

  <section class="slide slide--values">
    <h2 class="slide__header">Values &amp; Belief</h2>
    <div class="photo photo--compass" role="img" aria-label="Close-up photo of an antique brass compass on a chain resting on patterned fabric"></div>
    <div class="card card--values">
      <p class="card__lead">What are your deepest held values and beliefs?</p>
      <p>Our values and beliefs are what drive the direction of your life. Yet, most people never stop to seriously consider what their values and beliefs are.</p>
      <p>That’s why so many of us find ourselves wondering, “How did I get here?”</p>
      <p>Upon reflection, you may find that you’ve modeled your values and beliefs after those of the important people in your life, like your parents. Or, you may find that as you move through life, your values and beliefs changed.</p>
      <p>Unfortunately, it’s possible you’ll also discover you’ve been holding onto negative beliefs about yourself for years. Life coaching shines a bright light on where and how some of our negative belief patterns were adopted. Reversing any <span class="link">negative core beliefs</span> affecting your life will be instrumental in our work together.</p>
      <p>Once you know clearly your values and beliefs, it’ll be easier to be the person you want to be in all circumstances. And as you work to achieve your goals, you’ll make decisions that are closely aligned with <span class="link">your core values.</span> Ultimately, you’ll feel like you’re completely living a life of integrity.</p>
    </div>
  </section>

  <div class="slide-range">Slide 5 - 8</div>
</div>
</body>
</html>
```